依頼詳細
新規開設にあたり、入り口上の電飾看板のデザインをお願いしたいと思っています。キャッチコピーと施設名にシンプルなデザインをお願いいたします。
記載項目
看板
サイズ:縦730 横5600
内容:お子様の可能性を引き出すお手伝い 児童発達支援・放課後等デイサービス くるのえま朝霞 電話番号(未定)
希望イメージ
シンプル 複雑
単色 カラフル
暗い 明るい
日常 高級
遊び心 厳粛
未来的 伝統的
女性的 男性的
希望する色
青系、緑系、黄・オレンジ系
納品ファイル
• イラストレーター形式 (.ai)
• PNG形式 (.png)
補足説明
電話番号が決定しました。
048-555-0193
よろしくお願いいたします。
■ 選んだ理由

シンプルながらも星や可能性を伸ばすイメージが反映されていてよかったです。

■ 提案者全員のお礼・コメント

皆さまご提案ありがとうございます。
さまざまなデザインで弊社のイメージを具体化していただき大変嬉しく思います。
選ぶことが大変困難を極めましたが、決定させていただきました。
また機会がございましたら、何卒よろしくお願いいたします。

```html
<!DOCTYPE html>
<html lang="ja">
<head>
<meta charset="utf-8">
<title>くるのえま朝霞 入口看板</title>
<link rel="stylesheet" href="https://fonts.googleapis.com/css2?family=M+PLUS+Rounded+1c:wght@500;800&display=swap">
<style>
  :root {
    --page-bg: #eef0f2;
    --sign-white: #ffffff;
    --sky-blue: #5bb6e8;
    --sky-light: #cfe9f7;
    --sun-orange: #f08a1c;
    --leaf-green: #3f9a3a;
    --ink: #2a2a2a;
  }
  * { margin: 0; padding: 0; box-sizing: border-box; }
  html, body { width: 900px; height: 1200px; overflow: hidden; }
  body {
    background: var(--page-bg);
    font-family: "M PLUS Rounded 1c", sans-serif;
    position: relative;
  }
  .signboard {
    position: absolute;
    left: 20px; top: 544px;
    width: 860px; height: 112px;
    background: var(--sign-white);
    overflow: hidden;
    box-shadow: 0 2px 6px rgba(0,0,0,.15);
  }
  .signboard__sky { position: absolute; inset: 0; }
  .service-label {
    position: absolute; left: 22px; top: 10px;
    font-size: 11px; font-weight: 500; color: var(--sun-orange);
    letter-spacing: .04em;
  }
  .facility-name {
    position: absolute; left: 20px; top: 28px;
    display: flex; align-items: center; gap: 10px;
  }
  .facility-name__dot {
    width: 14px; height: 14px; border-radius: 50%;
    background: var(--sun-orange);
  }
  .facility-name__text {
    font-size: 50px; font-weight: 800; line-height: 1;
    color: var(--sun-orange); letter-spacing: .02em;
  }
  .contact {
    position: absolute; right: 22px; top: 22px; text-align: right;
  }
  .contact__catch {
    font-size: 10px; font-weight: 500; color: var(--leaf-green);
    line-height: 1.4;
  }
  .contact__phone {
    margin-top: 4px;
    display: flex; align-items: center; justify-content: flex-end; gap: 6px;
    font-size: 26px; font-weight: 800; color: var(--ink); letter-spacing: .02em;
  }
  .contact__phone svg { width: 24px; height: 24px; }
</style>
</head>
<body>
  <div class="signboard">
    <svg class="signboard__sky" viewBox="0 0 860 112" preserveAspectRatio="none" aria-hidden="true">
      <path d="M640 0 H860 V30 C820 20 790 36 760 26 C730 14 700 24 670 12 C660 8 650 4 640 0 Z" fill="var(--sky-light)"/>
      <path d="M0 98 C180 88 360 104 560 94 C700 88 790 96 860 92 V112 H0 Z" fill="var(--sky-blue)"/>
    </svg>
    <p class="service-label">児童発達支援・放課後等デイサービス</p>
    <div class="facility-name">
      <span class="facility-name__dot"></span>
      <span class="facility-name__text">くるのえま朝霞</span>
    </div>
    <div class="contact">
      <p class="contact__catch">お子様の可能性を引き出すお手伝い</p>
      <p class="contact__catch">児童発達支援・放課後等デイサービス</p>
      <p class="contact__phone">
        <svg viewBox="0 0 24 24" aria-hidden="true"><path fill="var(--ink)" d="M6.6 10.8a15.1 15.1 0 0 0 6.6 6.6l2.2-2.2a1 1 0 0 1 1-.25 11.4 11.4 0 0 0 3.6.57 1 1 0 0 1 1 1V20a1 1 0 0 1-1 1A17 17 0 0 1 3 4a1 1 0 0 1 1-1h3.5a1 1 0 0 1 1 1c0 1.25.2 2.46.57 3.6a1 1 0 0 1-.25 1z"/></svg>
        048-555-0193
      </p>
    </div>
  </div>
</body>
</html>
```